New Invitation Design Project

We are looking for someone to design our e-vite, save the date and wine labels for our upcoming event on June 26th. Our event is an open house for our current clients and business colleagues to show our appreciation for them. We want to incorporate our new logo. We would like a professional but fun invitation with multiple versions in different manners of the design we choose.

Industry/Entity Type

House

```html
<!DOCTYPE html>
<html lang="en">
<head>
<meta charset="utf-8">
<title>HRB Open House Invitation – Colour Variants</title>
<link rel="stylesheet" href="https://fonts.googleapis.com/css2?family=Alfa+Slab+One&family=Montserrat:ital,wght@0,400;0,600;0,800;1,800;1,900&family=Oswald:wght@400&display=swap">
<style>
  :root {
    --ink: #2d3e4a;
    --ink-soft: #3c4f5c;
    --headline-gold: #e8d21a;
    --headline-blue: #1a76d8;
    --headline-red: #e3261b;
    --star-white: #ffffff;
    --rule: #7a5a20;
  }
  html, body {
    margin: 0;
    padding: 0;
    width: 1200px;
    height: 853px;
    overflow: hidden;
    background: #ffffff;
  }
  .sheet {
    position: relative;
    width: 1200px;
    height: 853px;
  }
  .card {
    position: absolute;
    width: 597px;
    height: 423px;
    box-sizing: border-box;
    border: 9px solid var(--frame);
    background: var(--paper);
    font-family: "Montserrat", sans-serif;
    color: var(--ink);
    overflow: hidden;
  }
  .card > * { position: absolute; margin: 0; }

  .v-green  { left: 0;     top: 0;   --frame: #4a6fb5; --paper: #a9cf44; --time: #1a6fe0; --drop-bg: #a9cf44; --rule: #8a9a40; --rsvp: #f4f046; }
  .v-sunset { left: 603px; top: 0;   --frame: #12302a; --paper: linear-gradient(180deg, #ef7f12 0%, #f7a915 45%, #fde11f 100%); --time: #1a55e0; --drop-bg: #f59a12; --rule: #a0300f; --rsvp: #fff04a; }
  .v-amber  { left: 0;     top: 430px; --frame: #2aa8ae; --paper: #f3b21b; --time: #2ab7e8; --drop-bg: #f3b21b; --rule: #a55c16; --rsvp: #fff04a; }
  .v-mono   { left: 603px; top: 430px; --frame: #262626; --paper: #6e6e6e; --time: #7a7a7a; --drop-bg: #5e5e5e; --rule: #4a4a4a; --rsvp: #888888; --ink: #1c1c1c; --ink-soft: #262626;
              --headline-gold: #5a5a5a; --headline-blue: #5a5a5a; --headline-red: #5a5a5a; }

  .headline {
    left: 0; right: 0; top: 18px;
    text-align: center;
    font-family: "Alfa Slab One", serif;
    font-size: 19px;
    letter-spacing: 0.5px;
    text-shadow: 0 0 6px rgba(255,240,120,.9);
  }
  .v-mono .headline { text-shadow: 0 1px 0 #888; }
  .headline .gold { color: var(--headline-gold); }
  .headline .blue { color: var(--headline-blue); }
  .headline .red  { color: var(--headline-red); }

  .brand-box {
    left: 28px; top: 52px;
    width: 494px; height: 94px;
    border: 1.5px dashed rgba(60,60,40,.55);
  }
  .brand-name {
    left: 46px; top: 82px;
    display: flex; align-items: center; gap: 10px;
    font-weight: 600;
    font-size: 21px;
    color: var(--ink);
  }
  .brand-name .dot {
    width: 18px; height: 18px; border-radius: 50%;
    background: var(--ink);
  }
  .tagline {
    right: 34px; top: 56px;
    text-align: right;
    font-family: "Oswald", sans-serif;
    font-size: 21px;
    line-height: 30px;
    color: #111;
  }

  .drink {
    left: 36px; top: 160px;
    width: 400px; text-align: center;
    font-weight: 800;
    font-size: 17px;
    color: var(--star-white);
    letter-spacing: .3px;
  }
  .date {
    left: 20px; top: 188px;
    width: 430px; text-align: center;
    font-family: "Alfa Slab One", serif;
    font-size: 24px;
    color: #d9c36a;
    text-shadow: 0 1px 0 #fff, 0 2px 2px rgba(0,0,0,.35);
    letter-spacing: .5px;
  }
  .v-green .date { color: #c8c98a; }
  .v-mono  .date { color: #777; }
  .time {
    left: 20px; top: 222px;
    width: 410px; text-align: center;
    font-family: "Alfa Slab One", serif;
    font-size: 25px;
    color: var(--time);
    text-shadow: 0 1px 0 rgba(255,255,255,.7);
  }
  .drop-badge {
    left: 466px; top: 160px;
    width: 84px; height: 90px;
    box-sizing: border-box;
    border: 2px solid rgba(120,90,30,.6);
    background: var(--drop-bg);
    display: flex; align-items: center; justify-content: center;
    text-align: center;
    font-weight: 900; font-style: italic;
    font-size: 16px; line-height: 19px;
    color: #fff;
    text-shadow: 0 0 2px rgba(0,0,0,.45);
  }
  .v-sunset .drop-badge { border-color: #b02a10; }
  .v-mono .drop-badge { border-color: #ccc; }

  .rsvp {
    left: 0; width: 579px; top: 262px;
    text-align: center;
    font-weight: 600;
    font-size: 16px;
    color: var(--ink);
  }
  .rsvp .label { color: var(--rsvp); }
  .rule {
    left: 20px; width: 538px; height: 2px;
    background: var(--rule);
  }
  .rule.upper { top: 288px; }
  .rule.lower { top: 374px; }

  .firm-details, .address {
    top: 303px;
    font-size: 15.5px;
    line-height: 21.5px;
    color: var(--ink-soft);
  }
  .firm-details { left: 22px; }
  .address { right: 28px; text-align: right; }
  .website {
    left: 0; width: 579px; top: 378px;
    text-align: center;
    font-size: 15.5px;
    color: var(--ink-soft);
  }
</style>
</head>
<body>
<main class="sheet">

  <section class="card v-green">
    <h1 class="headline"><span class="gold">YOU'RE INVITED</span> <span class="blue">TO THE HRB</span> <span class="red">OPEN HOUSE!</span></h1>
    <div class="brand-box"></div>
    <div class="brand-name"><span class="dot"></span>Hollis Reed Barrow</div>
    <p class="tagline">Meet our Newest Staff Members<br>and Attorneys Network with<br>Our Fabulous Guests</p>
    <p class="drink">☆ ☆ ☆ HAVE A DRINK ON US! ☆ ☆ ☆</p>
    <p class="date">THURSDAY, JUNE 26, 2014</p>
    <p class="time">3:00PM - 7:00PM</p>
    <div class="drop-badge">DROP<br>BY<br>ANY<br>TIME!</div>
    <p class="rsvp"><span class="label">RSVP</span> TO MLARSEN@HRBLEGAL.COM OR (847) 555-0142</p>
    <div class="rule upper"></div>
    <p class="firm-details">HOLLIS, REED &amp; BARROW<br>ATTORNEYS AT LAW<br>847-555-0142</p>
    <p class="address">1250 MEADOWBROOK ROAD<br>SUITE 210,<br>LAKEVIEW PARK, IL 60099</p>
    <div class="rule lower"></div>
    <p class="website">WWW. HRBLEGAL.COM</p>
  </section>

  <section class="card v-sunset">
    <h1 class="headline"><span class="gold">YOU'RE INVITED</span> <span class="blue">TO THE HRB</span> <span class="red">OPEN HOUSE!</span></h1>
    <div class="brand-box"></div>
    <div class="brand-name"><span class="dot"></span>Hollis Reed Barrow</div>
    <p class="tagline">Meet our Newest Staff Members<br>and Attorneys Network with<br>Our Fabulous Guests</p>
    <p class="drink">☆ ☆ ☆ HAVE A DRINK ON US! ☆ ☆ ☆</p>
    <p class="date">THURSDAY, JUNE 26, 2014</p>
    <p class="time">3:00PM - 7:00PM</p>
    <div class="drop-badge">DROP<br>BY<br>ANY<br>TIME!</div>
    <p class="rsvp"><span class="label">RSVP</span> TO MLARSEN@HRBLEGAL.COM OR (847) 555-0142</p>
    <div class="rule upper"></div>
    <p class="firm-details">HOLLIS, REED &amp; BARROW<br>ATTORNEYS AT LAW<br>847-555-0142</p>
    <p class="address">1250 MEADOWBROOK ROAD<br>SUITE 210,<br>LAKEVIEW PARK, IL 60099</p>
    <div class="rule lower"></div>
    <p class="website">WWW. HRBLEGAL.COM</p>
  </section>

  <section class="card v-amber">
    <h1 class="headline"><span class="gold">YOU'RE INVITED</span> <span class="blue">TO THE HRB</span> <span class="red">OPEN HOUSE!</span></h1>
    <div class="brand-box"></div>
    <div class="brand-name"><span class="dot"></span>Hollis Reed Barrow</div>
    <p class="tagline">Meet our Newest Staff Members<br>and Attorneys Network with<br>Our Fabulous Guests</p>
    <p class="drink">☆ ☆ ☆ HAVE A DRINK ON US! ☆ ☆ ☆</p>
    <p class="date">THURSDAY, JUNE 26, 2014</p>
    <p class="time">3:00PM - 7:00PM</p>
    <div class="drop-badge">DROP<br>BY<br>ANY<br>TIME!</div>
    <p class="rsvp"><span class="label">RSVP</span> TO MLARSEN@HRBLEGAL.COM OR (847) 555-0142</p>
    <div class="rule upper"></div>
    <p class="firm-details">HOLLIS, REED &amp; BARROW<br>ATTORNEYS AT LAW<br>847-555-0142</p>
    <p class="address">1250 MEADOWBROOK ROAD<br>SUITE 210,<br>LAKEVIEW PARK, IL 60099</p>
    <div class="rule lower"></div>
    <p class="website">WWW. HRBLEGAL.COM</p>
  </section>

  <section class="card v-mono">
    <h1 class="headline"><span class="gold">YOU'RE INVITED</span> <span class="blue">TO THE HRB</span> <span class="red">OPEN HOUSE!</span></h1>
    <div class="brand-box"></div>
    <div class="brand-name"><span class="dot"></span>Hollis Reed Barrow</div>
    <p class="tagline">Meet our Newest Staff Members<br>and Attorneys Network with<br>Our Fabulous Guests</p>
    <p class="drink">☆ ☆ ☆ HAVE A DRINK ON US! ☆ ☆ ☆</p>
    <p class="date">THURSDAY, JUNE 26, 2014</p>
    <p class="time">3:00PM - 7:00PM</p>
    <div class="drop-badge">DROP<br>BY<br>ANY<br>TIME!</div>
    <p class="rsvp"><span class="label">RSVP</span> TO MLARSEN@HRBLEGAL.COM OR (847) 555-0142</p>
    <div class="rule upper"></div>
    <p class="firm-details">HOLLIS, REED &amp; BARROW<br>ATTORNEYS AT LAW<br>847-555-0142</p>
    <p class="address">1250 MEADOWBROOK ROAD<br>SUITE 210,<br>LAKEVIEW PARK, IL 60099</p>
    <div class="rule lower"></div>
    <p class="website">WWW. HRBLEGAL.COM</p>
  </section>

</main>
</body>
</html>
```